Local Electrical company need some kick ass business cards

In need of some in your face design business cards for a family owned electrical service company in Edmonton, Alberta Canada. We provide reliable and trustworthy electrical service for commercial and residential work in the Edmonton and area. We have been in business for 25 years.

Target Market(s)

Residential and commercial electrical

Industry/Entity Type

Business

Contact Information for Business Card

Your welcome to change and modify the brightway electric logo. please include the lightbulb! Our Colours are black and green please stay with that.
Please include a name phone number and address on the card
phone number - 780-318-5062
#22, 418 Maple Cres, St.Albert, Alberta.
Two things that need to be on the card.
"your friendly neighborhood electrictrician"
Commercial & residential electrical repair and service

Colors
9bcb3c

Requirements
Must have
• Light bulb guy Attached
• "your friendly neighborhood electrictrician"
• Commercial & residential electrical repair and service
• phone number - 780-318-5062
• #22, 418 Maple Cres, St.Albert, Alberta.
• Our colours are black and green
Nice to have
• go wild i want something loud

```html
<!DOCTYPE html>
<html lang="en">
<head>
<meta charset="utf-8">
<title>Brightway Electric – Business Card</title>
<link rel="stylesheet" href="https://fonts.googleapis.com/css2?family=Lato:wght@300;400;700;900&display=swap">
<style>
  :root {
    --bg: #d8d8d4;
    --green: #9bcb3c;
    --green-deep: #4f8a10;
    --green-dark: #2f5a08;
    --black: #111111;
    --ink: #1c1c1c;
    --white: #ffffff;
    --paper: #f7f7f7;
    --mist: #e6ece0;
  }
  * { margin: 0; padding: 0; box-sizing: border-box; }
  html, body {
    width: 1200px; height: 871px; overflow: hidden;
    background: var(--bg);
    font-family: "Lato", Arial, sans-serif;
  }
  .card {
    position: absolute;
    left: 270px;
    width: 660px; height: 377px;
    overflow: hidden;
    box-shadow: 0 6px 18px rgba(0,0,0,0.25);
  }
  /* Front face */
  .card-front {
    top: 40px;
    background: linear-gradient(110deg, var(--black) 0%, var(--green-dark) 38%, var(--green-deep) 70%, #5f9a18 100%);
  }
  .mascot {
    position: absolute; left: 60px; top: 45px;
    width: 190px; height: 300px;
    border-radius: 90px 90px 30px 30px;
    background: radial-gradient(circle at 50% 35%, #eef7f4 0%, #cfe2dc 45%, var(--green) 75%, rgba(155,203,60,0) 100%);
  }
  .tagline {
    position: absolute; left: 290px; top: 120px;
    color: #dcdcdc;
  }
  .tagline-lead { font-size: 50px; font-weight: 300; line-height: 1; letter-spacing: 0.5px; }
  .tagline-sub { font-size: 23px; font-weight: 400; line-height: 1.4; color: #e9f2dc; }

  /* Back face */
  .card-back {
    top: 457px;
    background: linear-gradient(135deg, var(--white) 0%, var(--paper) 60%, var(--mist) 100%);
  }
  .contact { position: absolute; left: 70px; top: 92px; color: var(--ink); }
  .contact-name {
    font-size: 23px; font-weight: 900; color: var(--green);
    font-variant: small-caps; letter-spacing: 1.5px; line-height: 1;
  }
  .contact-role { font-size: 13px; margin-top: 4px; }
  .contact-list { list-style: none; margin-top: 22px; font-size: 14px; }
  .contact-list li { display: flex; align-items: center; gap: 10px; height: 24px; }
  .contact-list svg { width: 13px; height: 13px; flex: none; }
  .contact-address { padding-left: 0; }
  .brand {
    position: absolute; right: 50px; top: 105px;
    display: flex; align-items: center; gap: 12px;
  }
  .brand-dot { width: 22px; height: 22px; border-radius: 50%; background: var(--green); }
  .brand-name {
    font-size: 30px; font-weight: 900; color: var(--black);
    line-height: 1;
  }
  .service-band {
    position: absolute; left: 0; right: 0; bottom: 0; height: 74px;
    background: var(--black);
    border-top: 5px solid var(--green);
    color: var(--white);
    font-size: 15px; letter-spacing: 0.3px;
    display: flex; align-items: center; padding-left: 120px;
  }
</style>
</head>
<body>
  <section class="card card-front">
    <div class="mascot" role="img" aria-label="Cartoon light bulb character wearing a green cap, waving"></div>
    <div class="tagline">
      <p class="tagline-lead">your friendly</p>
      <p class="tagline-sub">neighborhood electrictrician</p>
    </div>
  </section>

  <section class="card card-back">
    <div class="contact">
      <h1 class="contact-name">Dale Harmon</h1>
      <p class="contact-role">President</p>
      <ul class="contact-list">
        <li class="contact-address">#22, 418 Maple Cres, St.Albert, Alberta.</li>
        <li>
          <svg viewBox="0 0 16 16" aria-hidden="true"><path d="M3 1h3l1.5 4-2 1.2a9 9 0 0 0 4.3 4.3L11 8.5l4 1.5v3a2 2 0 0 1-2 2A12 12 0 0 1 1 3a2 2 0 0 1 2-2z" fill="#9bcb3c"/></svg>
          780-318-5062
        </li>
        <li>
          <svg viewBox="0 0 16 16" aria-hidden="true"><rect x="1" y="3" width="14" height="10" rx="1" fill="none" stroke="#9bcb3c" stroke-width="1.6"/><path d="M1.5 4l6.5 5 6.5-5" fill="none" stroke="#9bcb3c" stroke-width="1.6"/></svg>
          support@brightway.com
        </li>
      </ul>
    </div>
    <div class="brand">
      <span class="brand-dot"></span>
      <span class="brand-name">Brightway Electric</span>
    </div>
    <p class="service-band">Commercial &amp; residential electrical repair and service</p>
  </section>
</body>
</html>
```